Hemp (cannabis) CBD Oil 3-page Blog website

The objective is 1) to look like professional/serious company, 2) to get investors excited about our Hemp business, 3) to get investor email and phone numbers and build a sense community. Potential investors should become excited that this is their “window of opportunity,” because VeltoriKa is made up of extraordinary people who all have made successful business before, that the location in Uruguay is a huge benefit, that we will become the biggest and best CBD-oil manufacturer in Latin America, and that we focus on all-legal medicinal CBD oil extracted from hemp.

Target Market(s)

Potential investors looking to invest between $30,000-$1,000,000 USD into a HEMP startup business, based in Uruguay, South America.

Industry/Entity Type

Business

Number of Pages Required

3 page

Font styles to use
Sans Serif

Requirements
Must have
• Three pages: Home, Members Only, News (blog).
• FOR MORE DETAIL SEE ATTACHED WORD REQUIREMENTS DOCUMENT.
Nice to have
• Uruguay colors: sky blue, golden sun. Medicinal. Legal. Mainstream. Hemp. Professional people. Opportunity/Money/Investor. Uruguay. Latin America. 1st to Market.
Should not have
• Marijuana (HEMP yes, marijuana NO), anything that looks illegal.

```html
<!DOCTYPE html>
<html lang="en">
<head>
<meta charset="utf-8">
<title>VeltoriKa — CBD Oil Manufacturer</title>
<link href="https://fonts.googleapis.com/css2?family=Open+Sans:wght@400;600;700&display=swap" rel="stylesheet">
<style>
:root{
  --orange:#f5a31a;
  --gold:#f2bc3a;
  --green:#7ab648;
  --blue:#1d62ad;
  --brand-blue:#1f6fb5;
  --dark:#231f20;
  --text:#555555;
  --heading:#222222;
  --light-line:#e4e4e4;
  --card-grey:#ebebeb;
  --arrow-grey:#6d6d6d;
}
*{margin:0;padding:0;box-sizing:border-box}
html,body{width:1200px;height:2500px;overflow:hidden}
body{font-family:"Open Sans",Arial,sans-serif;color:var(--text);background:#fff;position:relative}
.abs{position:absolute}

/* header */
.site-header{position:absolute;left:0;top:0;width:1200px;height:95px;background:#fff}
.logo{position:absolute;left:208px;top:45px;display:flex;align-items:center;gap:8px}
.logo-dot{width:14px;height:14px;border-radius:50%;background:var(--green)}
.logo-name{font-size:24px;font-weight:600;color:var(--brand-blue);letter-spacing:.2px;line-height:28px}
.top-contact{position:absolute;right:210px;top:21px;font-size:11px;color:#333;display:flex;align-items:center;gap:7px}
.top-contact svg{width:11px;height:11px}
.top-contact .sep{color:#999}
.main-nav{position:absolute;left:480px;top:54px;display:flex;gap:22px;font-size:11px;color:#333;font-weight:600}
.main-nav a{color:inherit;text-decoration:none;padding-bottom:4px}
.main-nav a.active{color:var(--green);border-bottom:2px solid var(--green)}
.social{display:flex;gap:6px}
.social span{width:16px;height:16px;border-radius:50%;background:#8a8a8a;display:block}
.header-social{position:absolute;left:893px;top:53px}

/* hero */
.hero{position:absolute;left:0;top:95px;width:1200px;height:405px;
  background:radial-gradient(ellipse at 60% 45%,#3e7a2c 0%,#285a1e 40%,#173816 75%,#0f2410 100%)}
.hero-shade{position:absolute;inset:0;background:rgba(0,0,0,.18)}
.hero-title{position:absolute;left:0;width:1200px;top:232px;text-align:center;color:#fff;font-size:26px;font-weight:400}
.hero-title em{font-style:normal;color:var(--orange)}
.hero-sub{position:absolute;left:320px;width:560px;top:270px;text-align:center;color:#fff;font-size:12.5px;line-height:16px}
.btn{display:inline-block;background:var(--orange);color:#fff;font-size:12px;text-align:center}
.hero-btn{position:absolute;left:537px;top:327px;width:126px;height:29px;line-height:29px}
.arrow{position:absolute;width:26px;height:26px;border-radius:50%;display:flex;align-items:center;justify-content:center}
.arrow.prev{background:var(--arrow-grey)}
.arrow.next{background:var(--orange)}
.arrow svg{width:12px;height:12px}

/* section heading with offset frame */
.sec-title{position:absolute;font-size:21px;font-weight:600;color:var(--heading)}
.title-frame{position:absolute;border:5px solid var(--light-line)}

/* about */
.about-text{position:absolute;left:208px;top:636px;width:325px;font-size:11px;line-height:17px;color:#666}
.about-text p{margin-bottom:17px}
.about-btn{position:absolute;left:208px;top:910px;width:116px;height:28px;line-height:28px}
.process-graphic{position:absolute;left:637px;top:572px;width:356px;height:356px;border-radius:50%;
  background:radial-gradient(circle at 50% 50%,#f2bc2a 0%,#f2bc2a 22%,#e9a23a 40%,#c9734a 62%,#5f9a86 100%)}

/* team */
.team{position:absolute;left:0;top:995px;width:1200px;height:405px;background:var(--dark);overflow:hidden}
.team-watermark{position:absolute;left:-10px;top:130px;font-size:100px;font-weight:700;color:rgba(255,255,255,.05);letter-spacing:2px}
.team .sec-title{color:#fff;left:208px;top:100px}
.team .title-frame{left:292px;top:90px;width:58px;height:52px;border-color:#4a4647}
.team-text{position:absolute;left:208px;top:170px;width:220px;font-size:11px;line-height:17px;color:#ddd}
.team-rule{position:absolute;left:208px;top:257px;width:85px;height:1px;background:#6b6768}
.member{position:absolute;width:156px;height:149px}
.member.tone-a{background:linear-gradient(160deg,#5a4a3f,#8c7360 60%,#3e332c)}
.member.tone-b{background:linear-gradient(160deg,#7a6654,#b89a7c 55%,#4a3a2e)}
.member.tone-c{background:linear-gradient(160deg,#6d7564,#a39a85 55%,#3c3a33)}
.member.tone-d{background:linear-gradient(160deg,#4d5a3c,#86876a 55%,#2e3326)}
.member.tone-e{background:linear-gradient(160deg,#3d3a36,#7c6e62 55%,#232120)}
.member.highlight{background:#8a8a82}
.member-card{position:absolute;left:11px;top:10px;width:134px;height:134px;background:#7fc243;color:#fff;text-align:center;display:flex;flex-direction:column;justify-content:center}
.member-card .name{font-size:12px;font-weight:600}
.member-card .role{font-size:9px;margin-top:4px}

/* news */
.news .sec-title{left:0;width:1200px;text-align:center;top:1475px}
.news-card{position:absolute;width:247px}
.news-card.featured{background:#fff;box-shadow:0 0 8px rgba(0,0,0,.15)}
.news-card.plain{background:var(--card-grey)}
.news-img{height:175px}
.news-body{padding:18px 22px}
.news-title{font-size:12.5px;font-weight:700;color:var(--blue);line-height:17px}
.news-meta{font-size:9px;color:var(--orange);margin-top:8px;display:flex;gap:8px}
.news-excerpt{font-size:10px;line-height:14px;color:#888;margin-top:6px}
.read-more{font-size:10px;color:var(--green);margin-top:14px;display:block}

/* investor band */
.cta{position:absolute;left:0;top:1995px;width:1200px;height:85px}
.cta svg{position:absolute;left:0;top:0}
.cta-text{position:absolute;left:207px;top:28px;font-size:17px;font-weight:700;color:#fff}
.cta-btn{position:absolute;left:850px;top:29px;width:142px;height:28px;border:1px solid #fff;color:#fff;font-size:11.5px;text-align:center;line-height:26px}

/* footer */
.footer-left{position:absolute;left:0;top:2080px;width:610px;height:420px;background:var(--dark)}
.footer-right{position:absolute;left:610px;top:2080px;width:590px;height:420px;
  background:radial-gradient(ellipse at 40% 40%,#3a4a2c 0%,#25301d 45%,#171c13 100%)}
.footer-right .shade{position:absolute;inset:0;background:rgba(0,0,0,.35)}
.footer-left .sec-title{color:#fff;left:208px;top:60px}
.footer-left .title-frame{left:250px;top:45px;width:103px;height:52px;border-color:#4a4647}
.contact-list{position:absolute;left:208px;top:125px;font-size:11px;line-height:16px;color:#ddd}
.contact-list dt{font-weight:700;color:#fff}
.contact-list dd{margin-bottom:11px}
.footer-social{position:absolute;left:208px;top:327px}
.copyright{position:absolute;left:208px;top:364px;font-size:11px;color:#ddd}
.copyright b{font-weight:400;color:var(--orange)}
.contact-form{position:absolute;left:658px;top:2150px;width:334px}
.field{height:55px;border-bottom:1px solid rgba(255,255,255,.35);font-size:11px;color:#fff;padding-top:4px}
.field.tall{height:100px}
.submit{position:absolute;left:0;top:257px;width:86px;height:27px;line-height:27px;background:var(--orange);color:#fff;font-size:11px;text-align:center}
</style>
</head>
<body>

<header class="site-header">
  <div class="logo"><span class="logo-dot"></span><span class="logo-name">VeltoriKa</span></div>
  <div class="top-contact">
    <svg viewBox="0 0 12 12"><path d="M2.5 1l2 2.5-1.2 1.3c.7 1.6 2 2.9 3.6 3.6L8.2 7l2.5 2-1 2C5 10.6 1.4 7 1 2.3z" fill="#7ab648"/></svg>
    <span>USA &nbsp;(+1) 555.010.0127</span><span class="sep">/</span><span>UY &nbsp;(+54) 911.0000.1234</span>
    <svg viewBox="0 0 12 12" style="margin-left:12px"><rect x="1" y="2.5" width="10" height="7" fill="#7ab648"/><path d="M1 2.5l5 4 5-4" stroke="#fff" fill="none"/></svg>
    <span>hello@veltorika-mail.example</span>
  </div>
  <nav class="main-nav">
    <a class="active">Home</a><a>About</a><a>Members Only</a><a>Team</a><a>News</a><a>Contact</a>
  </nav>
  <div class="social header-social"><span></span><span></span><span></span><span></span></div>
</header>

<section class="hero">
  <div class="abs" role="img" aria-label="Close-up photo of green hemp leaves" style="inset:0"></div>
  <div class="hero-shade"></div>
</section>
<h1 class="hero-title">VeltoriKa best <em>CBD-oil manufacturer</em></h1>
<p class="hero-sub">Our hemp was enginnered to maximize therapeutic CBD. Under Uruguyan laws we refine the oil at 2x higher profitability than anywhere else in the world.</p>
<a class="btn hero-btn">Discover More</a>
<div class="arrow prev" style="left:157px;top:284px"><svg viewBox="0 0 12 12"><path d="M11 6H2M5 3L2 6l3 3" stroke="#fff" stroke-width="1.5" fill="none"/></svg></div>
<div class="arrow next" style="left:1034px;top:284px"><svg viewBox="0 0 12 12"><path d="M1 6h9M7 3l3 3-3 3" stroke="#fff" stroke-width="1.5" fill="none"/></svg></div>

<section class="about">
  <div class="title-frame" style="left:242px;top:560px;width:103px;height:52px"></div>
  <h2 class="sec-title" style="left:208px;top:573px">About Us</h2>
  <div class="about-text">
    <p>Our hemp was enginnered to maximize therapeutic CBD. Under Uruguyan laws we refine the oil at 2x higher profitability than anywhere else in the world.</p>
    <p>Lorem Ipsum is simply dummy text of the printing and typesetting industry. Lorem Ipsum has been the industry's standard dummy text ever since the 1500s, when an unknown printer took a galley of type and scrambled it to make a type specimen book. It has survived not only five centuries, but also the leap into electronic typesetting, remaining essentially.</p>
    <p>Our hemp was enginnered to maximize therapeutic CBD. Under Uruguyan laws we refine the oil at 2x higher profitability than anywhere else in the world.</p>
  </div>
  <a class="btn about-btn">Explore More &#10140;</a>
  <div class="process-graphic" role="img" aria-label="Process infographic: CBD at the centre, surrounded by hemp cultivation, extraction, oil refinement, therapeutic products, new markets and genetic engineering"></div>
</section>

<section class="team">
  <div class="team-watermark">MEMBERS</div>
  <div class="title-frame"></div>
  <h2 class="sec-title">Our Team</h2>
  <p class="team-text">Our team is composed of experts, each an authority in their field. And each of us has a successful record of starting business.</p>
  <div class="team-rule"></div>
  <div class="member tone-b" style="left:478px;top:45px" role="img" aria-label="Portrait photo of a team member"></div>
  <div class="member highlight" style="left:657px;top:45px" role="img" aria-label="Portrait photo of Daniel Reyes">
    <div class="member-card"><span class="name">Daniel Reyes</span><span class="role">Business Development</span></div>
  </div>
  <div class="member tone-a" style="left:833px;top:45px" role="img" aria-label="Portrait photo of a team member"></div>
  <div class="member tone-c" style="left:478px;top:215px" role="img" aria-label="Portrait photo of a team member"></div>
  <div class="member tone-d" style="left:657px;top:215px" role="img" aria-label="Portrait photo of a team member"></div>
  <div class="member tone-e" style="left:833px;top:215px" role="img" aria-label="Portrait photo of a team member"></div>
</section>

<section class="news">
  <div class="title-frame" style="left:610px;top:1462px;width:60px;height:52px"></div>
  <h2 class="sec-title">Our News</h2>
  <div class="arrow prev" style="left:159px;top:1730px"><svg viewBox="0 0 12 12"><path d="M11 6H2M5 3L2 6l3 3" stroke="#fff" stroke-width="1.5" fill="none"/></svg></div>
  <div class="arrow next" style="left:1034px;top:1730px"><svg viewBox="0 0 12 12"><path d="M1 6h9M7 3l3 3-3 3" stroke="#fff" stroke-width="1.5" fill="none"/></svg></div>

  <article class="news-card featured" style="left:207px;top:1550px;height:375px">
    <div class="news-img" role="img" aria-label="Photo of a woman holding a tablet" style="background:linear-gradient(180deg,#f4f2ef,#e4ddd5)"></div>
    <div class="news-body">
      <h3 class="news-title">Lorem Ipsum is simply dummy text of the printing</h3>
      <div class="news-meta"><span>March 8, 2016</span><span>0 Comments</span></div>
      <p class="news-excerpt">Lorem ipsum dolor sit amet, consectetuer adipiscing elit, sed diam nonummy nibh dolor sit amet, consectetuer adipiscing elit....</p>
      <a class="read-more">Read More &#10140;</a>
    </div>
  </article>
  <article class="news-card plain" style="left:477px;top:1550px;height:375px">
    <div class="news-img" role="img" aria-label="Photo of a man with a tablet in an office" style="background:linear-gradient(160deg,#a8705a,#d9d4cc 55%,#8a8580)"></div>
    <div class="news-body">
      <h3 class="news-title">Lorem Ipsum is simply dummy text of the printing</h3>
      <div class="news-meta"><span>March 8, 2016</span><span>0 Comments</span></div>
      <p class="news-excerpt">Lorem ipsum dolor sit amet, consectetuer adipiscing elit, sed diam nonummy nibh dolor sit amet, consectetu elit....</p>
      <a class="read-more">Read More &#10140;</a>
    </div>
  </article>
  <article class="news-card plain" style="left:745px;top:1550px;height:375px">
    <div class="news-img" role="img" aria-label="Photo of a businessman reading on a sofa" style="background:linear-gradient(160deg,#b3aa9e,#8c8478 50%,#3f4858)"></div>
    <div class="news-body">
      <h3 class="news-title">Lorem Ipsum is simply dummy text of the printing</h3>
      <div class="news-meta"><span>March 8, 2016</span><span>0 Comments</span></div>
      <p class="news-excerpt">Lorem ipsum dolor sit amet, consectetuer adipiscing elit, sed diam nonummy nibh dolor sit amet, consectetuer ....</p>
      <a class="read-more">Read More &#10140;</a>
    </div>
  </article>
</section>

<section class="cta">
  <svg width="1200" height="85" viewBox="0 0 1200 85">
    <rect width="1200" height="85" fill="var(--blue)"/>
    <polygon points="0,0 800,0 755,85 0,85" fill="var(--orange)"/>
  </svg>
  <p class="cta-text">Potential investors between $30,000-$1,000,000 USD?</p>
  <a class="cta-btn">Become a Member</a>
</section>

<footer>
  <div class="footer-left">
    <div class="title-frame"></div>
    <h2 class="sec-title">Contact Us</h2>
    <dl class="contact-list">
      <dt>Location:</dt><dd>Montevideo, Uruguay</dd>
      <dt>Call Us:</dt><dd>USA &nbsp;(+1) 555.010.0127<br>UY &nbsp;&nbsp;(+54) 911.0000.1234</dd>
      <dt>Email:</dt><dd>info@veltorika.example</dd>
      <dt>Website:</dt><dd>www.veltorika.example.uy</dd>
    </dl>
    <div class="social footer-social"><span></span><span></span><span></span><span></span></div>
    <p class="copyright">Copyright © 2017 <b>VeltoriKa</b>. &nbsp;All Rights Reserved.</p>
  </div>
  <div class="footer-right" role="img" aria-label="Dark close-up photo of hemp flowers"><div class="shade"></div></div>
  <form class="contact-form">
    <div class="field">Your Name</div>
    <div class="field">Email</div>
    <div class="field">Phone</div>
    <div class="field tall">Message</div>
    <div class="submit">Sumbit &#10148;</div>
  </form>
</footer>

</body>
</html>
```